Awesome ecommerce store banner needed!

We need a sharp, clear, strong banner for one of our subcategory pages on http://www.brixmolt.com
We'd like to incorporate the following image. We'd like the background to be gray or black. We are replacing the Wireless Intercoms banner that is orange (we hate it).
WE do like our other banners, however, so please use them as reference:
SIze: 980 x 380
Two raw images of the intercom we'd like you to encorporate have been included. Choose one or the other depending on what you think would be best. If using the single angle, please duplicate it. We want two intercoms in the banner
Simple and Clean is key:
Text: Wireless Intercoms
Text Color: Can be white/off gray
Text Style: Please keep it clean in line with the website
Background: Black/gray/white

```html
<!DOCTYPE html>
<html lang="en">
<head>
<meta charset="utf-8">
<title>Wireless Intercoms – Brixmolt</title>
<link rel="stylesheet" href="https://fonts.googleapis.com/css2?family=Archivo:wdth,wght@62..125,800..900&family=Nunito+Sans:wght@400;700;800&display=swap">
<style>
  :root {
    --bg: #000000;
    --headline: #ffffff;
    --body-text: #f0f0f0;
    --button-top: #8a8a8a;
    --button-bottom: #4e4e4e;
    --button-text: #ffffff;
    --device-light: #c9c9c4;
    --device-mid: #9e9e9a;
    --device-dark: #242424;
  }
  html, body {
    margin: 0;
    padding: 0;
    width: 1200px;
    height: 465px;
    overflow: hidden;
    background: var(--bg);
  }
  .banner {
    position: relative;
    width: 1200px;
    height: 465px;
    background: var(--bg);
    overflow: hidden;
  }
  .headline {
    position: absolute;
    left: 34px;
    top: 36px;
    margin: 0;
    color: var(--headline);
    font-family: "Archivo", "Arial Black", sans-serif;
    font-weight: 900;
    font-stretch: 100%;
    text-transform: uppercase;
    line-height: 1;
  }
  .headline-main {
    display: block;
    font-size: 118px;
    letter-spacing: -3px;
  }
  .headline-sub {
    display: block;
    margin-top: -4px;
    padding-left: 4px;
    font-size: 76px;
    letter-spacing: -1.5px;
  }
  .tagline {
    position: absolute;
    left: 53px;
    top: 238px;
    margin: 0;
    color: var(--body-text);
    font-family: "Nunito Sans", "Helvetica Neue", sans-serif;
    font-weight: 400;
    font-size: 26px;
    line-height: 1.3;
    letter-spacing: -0.3px;
  }
  .shop-button {
    position: absolute;
    left: 53px;
    top: 364px;
    width: 250px;
    height: 58px;
    display: flex;
    align-items: center;
    justify-content: center;
    gap: 8px;
    border-radius: 4px;
    background: linear-gradient(to bottom, var(--button-top), var(--button-bottom));
    color: var(--button-text);
    font-family: "Nunito Sans", "Helvetica Neue", sans-serif;
    font-weight: 800;
    font-size: 29px;
    text-decoration: none;
  }
  .shop-button svg {
    width: 14px;
    height: 22px;
  }
  .product {
    position: absolute;
  }
  .product-back {
    left: 548px;
    top: 0;
    width: 410px;
    height: 310px;
  }
  .product-front {
    left: 748px;
    top: 36px;
    width: 452px;
    height: 429px;
  }
</style>
</head>
<body>
<main class="banner">
  <h1 class="headline">
    <span class="headline-main">Wireless</span>
    <span class="headline-sub">Intercoms</span>
  </h1>

  <p class="tagline">Browse Products That Make<br>Wireless Home Communication Easy!</p>

  <a class="shop-button" href="http://www.brixmolt.com">
    Shop Now
    <svg viewBox="0 0 14 22" aria-hidden="true"><path d="M3 3 L11 11 L3 19" fill="none" stroke="currentColor" stroke-width="4" stroke-linecap="round" stroke-linejoin="round"/></svg>
  </a>

  <svg class="product product-back" viewBox="0 0 410 310" role="img" aria-label="Product photo: wireless intercom unit with silver speaker grille, black control panel and antenna">
    <defs>
      <linearGradient id="unitFillBack" x1="0" y1="0" x2="1" y2="0">
        <stop offset="0" stop-color="var(--device-light)"/>
        <stop offset="0.55" stop-color="var(--device-mid)"/>
        <stop offset="0.6" stop-color="var(--device-dark)"/>
        <stop offset="1" stop-color="var(--device-dark)"/>
      </linearGradient>
    </defs>
    <path d="M4 150 L330 100 L402 118 L402 212 L90 300 L10 268 Z" fill="url(#unitFillBack)"/>
  </svg>

  <svg class="product product-front" viewBox="0 0 452 429" role="img" aria-label="Product photo: second wireless intercom unit with silver speaker grille, black control panel and antenna">
    <defs>
      <linearGradient id="unitFillFront" x1="0" y1="0" x2="1" y2="0">
        <stop offset="0" stop-color="var(--device-light)"/>
        <stop offset="0.55" stop-color="var(--device-mid)"/>
        <stop offset="0.6" stop-color="var(--device-dark)"/>
        <stop offset="1" stop-color="var(--device-dark)"/>
      </linearGradient>
    </defs>
    <path d="M6 252 L370 200 L452 218 L452 330 L110 429 L10 429 Z" fill="url(#unitFillFront)"/>
  </svg>
</main>
</body>
</html>
```